Simple Modern Label for a Coconut oil product

We need a label designed for Organic Coconut oil. We would like the label to convey the gourmet/high quality product. It should be modern and simple and look like an artisinal product. The label will need to contain all the basic label requirements - Independence list, place for nutrition facts, our company logo etc.
The label will ultimately be printed as oil proof, so it will have a glossy appearance.
I have includes some examples that I like and a file with the logo.

Product Container - Wide Mount Clear Glass Jar: 4.75 inches tall (base to the bottom of the lid) and 9.5 in circumference
Label: Can be 1 or 2 separate labels, round, square and rectangle are okay
No larger than 3 inches high and 9 inches long

Target Market(s)

Middle Age home chef

Industry/Entity Type

Product

Requirements
Must have
• - logo (Attached below, I have this in multiple formats, let me know if you need them)
• - 14 FL OZ (414mL)
• - ingredient: organic unrefined whole kernel virgin coconut oil,
• - Manufacturer: XXX Y St., anywhere, CA, 99999
• - Distributed by Meadowfern Naturals, P.O. Box 5521, Oakland, CA 94612 www.MeadowfernNaturals.example
• - Certified Organic by Company Name
• - Product of Sri Lanka
Nice to have
• - Nutrition Facts
Should not have
• Clutter

```html
<!DOCTYPE html>
<html lang="en">
<head>
<meta charset="utf-8">
<title>Organic Coconut Oil Labels</title>
<link href="https://fonts.googleapis.com/css2?family=Saira:wght@400;500;600&display=swap" rel="stylesheet">
<style>
  :root {
    --teal: #0e4d57;
    --teal-deep: #0b4650;
    --charcoal: #1f1f21;
    --navy: #1b2f5c;
    --ice: #cfe8ee;
    --paper: #ffffff;
    --badge-green: #7ab83f;
    --badge-ring: #9ccb5e;
    --rule: #0e4d57;
  }
  * { box-sizing: border-box; margin: 0; padding: 0; }
  html, body { width: 1200px; height: 1000px; overflow: hidden; background: var(--paper); }
  body { position: relative; font-family: "Saira", sans-serif; color: var(--teal); }

  .label {
    position: absolute;
    top: 204px;
    width: 390px;
    height: 592px;
    background: var(--paper);
    box-shadow: 0 0 4px rgba(0,0,0,0.18);
  }
  .label::before, .label::after {
    content: "";
    position: absolute;
    left: 0; right: 0;
    height: 4px;
    background-size: 8px 4px;
    background-repeat: repeat-x;
  }
  .label::before { top: -4px; background-image: radial-gradient(circle at 50% 100%, var(--paper) 3.5px, transparent 4px); }
  .label::after { bottom: -4px; background-image: radial-gradient(circle at 50% 0, #e9e9e9 3.5px, transparent 4px); }
  .label--front { left: 188px; }
  .label--back { left: 623px; }

  .brand { position: absolute; left: 0; right: 0; display: flex; align-items: center; justify-content: center; gap: 8px; }
  .brand__square { background: var(--ice); }
  .brand__name { color: var(--navy); font-weight: 600; white-space: nowrap; }
  .label--front .brand { top: 50px; }
  .label--front .brand__square { width: 40px; height: 40px; }
  .label--front .brand__name { font-size: 24px; }
  .label--back .brand { top: 40px; }
  .label--back .brand__square { width: 26px; height: 26px; }
  .label--back .brand__name { font-size: 16px; }

  .product-title { position: absolute; left: 0; right: 0; text-align: center; font-weight: 400; color: var(--teal); white-space: nowrap; }
  .label--front .product-title { top: 155px; font-size: 37px; }
  .label--back .product-title { top: 90px; font-size: 32px; }

  .front-band {
    position: absolute; left: 0; right: 0; top: 239px; bottom: 0;
    background: linear-gradient(90deg, var(--teal-deep) 0%, #0f3d45 30%, var(--charcoal) 50%, #0f3d45 70%, var(--teal-deep) 100%);
    clip-path: polygon(0 0, 50% 79px, 100% 0, 100% 100%, 0 100%);
  }
  .product-emblem {
    position: absolute; left: 153px; top: 210px; width: 84px; height: 86px;
    border-radius: 50%;
    background: var(--teal);
  }

  .front-ingredient { position: absolute; left: 0; right: 0; top: 346px; text-align: center; color: var(--paper); font-size: 22px; line-height: 32px; white-space: nowrap; }
  .net-volume { position: absolute; left: 134px; top: 524px; color: var(--paper); font-size: 15px; }
  .origin-badge { position: absolute; left: 279px; top: 486px; width: 92px; height: 92px; }

  .back-subtitle { position: absolute; left: 0; right: 0; top: 135px; text-align: center; font-size: 14px; line-height: 19px; }
  .facts-heading { position: absolute; left: 0; right: 0; top: 181px; text-align: center; font-size: 19px; font-weight: 400; }

  .nutrition { position: absolute; left: 53px; top: 212px; width: 284px; border-collapse: collapse; font-size: 12.5px; }
  .nutrition th { text-align: left; font-weight: 600; padding: 0 0 2px; border-bottom: 1px solid var(--rule); }
  .nutrition td { height: 21.6px; border-bottom: 1px solid var(--rule); vertical-align: bottom; padding-bottom: 2px; }
  .nutrition tr:last-child td { border-bottom: none; }
  .nutrition .dv { text-align: right; }

  .back-details { position: absolute; left: 0; right: 0; top: 478px; text-align: center; font-size: 12px; line-height: 16.2px; font-style: normal; }
</style>
</head>
<body>

<section class="label label--front">
  <div class="brand"><span class="brand__square"></span><span class="brand__name">Meadowfern Naturals</span></div>
  <h1 class="product-title">Organic Coconut Oil</h1>
  <div class="front-band" role="img" aria-label="Chevron band pattern in deep teal shading to charcoal"></div>
  <div class="product-emblem" role="img" aria-label="Oil drop emblem"></div>
  <p class="front-ingredient">Organic Unrefined<br>Whole Kernel Virgin Coconut Oil</p>
  <p class="net-volume">14 FL OZ (414mL)</p>
  <svg class="origin-badge" viewBox="0 0 92 92" role="img" aria-label="100% Organic, Product of Sri Lanka">
    <defs>
      <path id="badge-arc-top" d="M14 46 A32 32 0 0 1 78 46"/>
      <path id="badge-arc-bottom" d="M78 46 A32 32 0 0 1 14 46"/>
    </defs>
    <circle cx="46" cy="46" r="44" fill="var(--badge-green)" stroke="var(--paper)" stroke-width="3"/>
    <circle cx="46" cy="46" r="26" fill="none" stroke="var(--badge-ring)" stroke-width="1"/>
    <text font-family="Saira, sans-serif" font-size="9" fill="var(--paper)">
      <textPath href="#badge-arc-top" startOffset="50%" text-anchor="middle">Product of Srilanka</textPath>
    </text>
    <text font-family="Saira, sans-serif" font-size="9" fill="var(--paper)">
      <textPath href="#badge-arc-bottom" startOffset="50%" text-anchor="middle">Product of Srilanka</textPath>
    </text>
    <text x="46" y="50" text-anchor="middle" font-family="Saira, sans-serif" font-size="12" font-weight="500" fill="var(--paper)">100% Organic</text>
  </svg>
</section>

<section class="label label--back">
  <div class="brand"><span class="brand__square"></span><span class="brand__name">Meadowfern Naturals</span></div>
  <h2 class="product-title">Organic Coconut Oil</h2>
  <p class="back-subtitle">Organic Unrefined<br>Whole Kernel Virgin Coconut Oil</p>
  <h3 class="facts-heading">NUTRITION FACTS</h3>
  <table class="nutrition">
    <thead><tr><th colspan="2">Amount Per 1 tbsp (13.6 g)</th></tr></thead>
    <tbody>
      <tr><td>Calories 117</td><td class="dv"></td></tr>
      <tr><td>Total Fat 14 g</td><td class="dv">21%</td></tr>
      <tr><td>Saturated fat 12 g</td><td class="dv">60%</td></tr>
      <tr><td>Polyunsaturated fat 0.2 g</td><td class="dv"></td></tr>
      <tr><td>Monounsaturated fat 0.8 g</td><td class="dv"></td></tr>
      <tr><td>Cholesterol 0 mg</td><td class="dv">0%</td></tr>
      <tr><td>Sodium 0 mg</td><td class="dv">0%</td></tr>
      <tr><td>Total Carbohydrate 0 g</td><td class="dv">0%</td></tr>
      <tr><td>Dietary fiber 0 g</td><td class="dv">0%</td></tr>
      <tr><td>Sugar 0 g</td><td class="dv">0%</td></tr>
      <tr><td>Protein 0 g</td><td class="dv">0%</td></tr>
    </tbody>
  </table>
  <address class="back-details">
    Manufacturer: XXX Y St., Anywhere, CA, 99999<br>
    Distributed by Meadowfern Naturals, P.O. Box 5521,<br>
    Oakland, CA 94612<br>
    www.MeadowfernNaturals.example<br>
    Certified Organic by Company Name<br>
    Product of Sri Lanka
  </address>
</section>

</body>
</html>
```